Letterhead and matching envelope design for a dental office

We need a new stationary design, letterhead and envelope #10, for a dental office in Denver area. We are called Brightfield Dental. We want a simple and minimalistic design but not a boring design. I wish to have one good point that makes it look professional. I have attached our logo. Feel free to use either one. I want the design for letterhead and envelope look like a "matching pair" but not look the same. The envelope doesn't have to be white and it will have an address window on bottom left.

Target Market(s)

everyone who visits dentist (adults)

Industry/Entity Type

Dental

Font styles to use
Other font styles liked:
• close to font on logo or something that matches well

Requirements
Must have
• professional
• simple, minimalistic
• unique point that stands out
Nice to have
• matching but not same design for letterhead and envelope
Should not have
• not look like all the other boring designs
• no flowery, distracting feats

```html
<!DOCTYPE html>
<html lang="en">
<head>
<meta charset="utf-8">
<title>Brightfield Dental – Stationery</title>
<link href="https://fonts.googleapis.com/css2?family=Cinzel:wght@500&family=Open+Sans:wght@400;600&display=swap" rel="stylesheet">
<style>
  :root {
    --green: #43b64a;
    --ink: #2b2b2b;
    --paper: #ffffff;
    --backdrop: #b8b8b8;
    --rule: #9a9a9a;
  }
  * { margin: 0; padding: 0; box-sizing: border-box; }
  html, body { width: 1200px; height: 1200px; overflow: hidden; }
  body { background: var(--backdrop); position: relative; font-family: "Open Sans", Arial, sans-serif; }

  .letterhead {
    position: absolute; left: 28px; top: 180px; width: 618px; height: 890px;
    background: var(--paper);
  }
  .letterhead .brand-name {
    position: absolute; left: 38px; top: 104px;
    font-family: "Cinzel", Georgia, serif; font-weight: 500; font-size: 19px;
    letter-spacing: 2px; color: var(--green); white-space: nowrap;
  }
  .contact-block {
    position: absolute; left: 424px; top: 42px;
    border-left: 1px solid var(--rule); padding-left: 14px;
    font-size: 10.5px; line-height: 12px; color: var(--ink);
  }
  .contact-block .firm { color: var(--green); font-weight: 600; }
  .contact-block .lines { margin-top: 10px; }
  .contact-block .lines li { list-style: none; display: flex; align-items: center; gap: 6px; line-height: 15px; }
  .contact-block svg { width: 9px; height: 9px; fill: var(--green); flex: none; }
  .page-band { position: absolute; left: 0; right: 0; bottom: 0; height: 8px; background: var(--green); }

  .envelope-back {
    position: absolute; left: 612px; top: 388px; width: 558px; height: 264px;
    background: var(--paper);
  }
  .envelope-back .flap { position: absolute; left: 0; top: 0; width: 558px; height: 72px; }

  .envelope-front {
    position: absolute; left: 612px; top: 664px; width: 558px; height: 264px;
    background: var(--paper);
  }
  .envelope-front .brand-name {
    position: absolute; left: 20px; top: 68px;
    font-family: "Cinzel", Georgia, serif; font-weight: 500; font-size: 14px;
    letter-spacing: 1.5px; color: var(--green); white-space: nowrap;
  }
  .return-address {
    position: absolute; left: 20px; top: 215px;
    font-size: 9.5px; line-height: 11px; color: var(--ink);
  }
  .return-address .firm { color: var(--green); font-weight: 600; }
  .envelope-front .page-band { height: 6px; }
</style>
</head>
<body>
  <section class="letterhead">
    <div class="brand-name">Brightfield Dental</div>
    <address class="contact-block" style="font-style:normal">
      <div class="firm">BRIGHTFIELD DENTAL</div>
      <div>4820 Larkspur Ave Suite 210</div>
      <div>Northglenn , CO 80233</div>
      <ul class="lines">
        <li><svg viewBox="0 0 10 10"><path d="M2 0.5 L3.6 2.6 L2.7 3.6 Q3.6 5.6 6.4 7.3 L7.4 6.4 L9.5 8 L8.3 9.5 Q4.5 9.3 1.8 6 Q0.3 3.7 0.6 1.6 Z"/></svg>720-555-0142</li>
        <li><svg viewBox="0 0 10 10"><path d="M0 2 H10 V8.5 H0 Z M0.8 2.6 L5 5.6 L9.2 2.6" stroke="#fff" stroke-width="0.8"/></svg>hello@brightfielddental.com</li>
        <li><svg viewBox="0 0 10 10"><circle cx="5" cy="5" r="4.4" fill="none" stroke="#43b64a" stroke-width="0.9"/><path d="M0.6 5 H9.4 M5 0.6 V9.4" stroke="#43b64a" stroke-width="0.7" fill="none"/></svg>www.brightfielddental.com</li>
      </ul>
    </address>
    <div class="page-band"></div>
  </section>

  <section class="envelope-back">
    <svg class="flap" viewBox="0 0 558 72" aria-hidden="true">
      <polygon points="0,0 558,0 522,72 34,72" fill="var(--green)"/>
    </svg>
  </section>

  <section class="envelope-front">
    <div class="brand-name">Brightfield Dental</div>
    <div class="return-address">
      <div class="firm">BRIGHTFIELD DENTAL</div>
      <div>4820 Larkspur Ave Suite 210</div>
      <div>Northglenn , CO 80233</div>
    </div>
    <div class="page-band"></div>
  </section>
</body>
</html>
```